Beacon Chillworks business card design

We would like a new design for our business card as we have a new logo.
We need generic business card to give our customers with our office details - with the option of making it individualized for each manager

Target Market(s)

Companies and homeowners

Industry/Entity Type

Air Conditioning

Contact Information for Business Card

We are not sure if we want single or double sided it will depend on the design we choose

Colors
33a6d7
0255a3

Requirements
Must have
• Logo
• phone: (08) 8712 4590
• email: beaconserve@frostmail.example
• website: www.beaconchillworks.example.au
• AU61924
• BLD402613
Nice to have
• Address - Shed 5/218 Kestrel Rd, Port Larkin SA 5790

```html
<!DOCTYPE html>
<html lang="en">
<head>
<meta charset="utf-8">
<title>Beacon Chillworks business card</title>
<link href="https://fonts.googleapis.com/css2?family=Montserrat:wght@400;500;700&display=swap" rel="stylesheet">
<style>
  :root {
    --backdrop: #2b2b2b;
    --card: #0b0b0b;
    --ink: #ffffff;
    --ink-soft: #d9d9d9;
    --rule: #8a8a8a;
  }
  * { margin: 0; padding: 0; box-sizing: border-box; }
  html, body {
    width: 1200px; height: 900px; overflow: hidden;
    background: var(--backdrop);
    font-family: "Montserrat", sans-serif;
    color: var(--ink);
  }
  .sheet {
    width: 1200px; height: 900px;
    display: flex; flex-direction: column;
    align-items: center; justify-content: center; gap: 60px;
  }
  .card {
    position: relative;
    width: 560px; height: 320px;
    background: var(--card);
    border-radius: 18px;
    box-shadow: 0 10px 30px rgba(0,0,0,.45);
    overflow: hidden;
  }

  /* contact side */
  .card--contact { text-align: center; }
  .person-name {
    position: absolute; top: 38px; left: 0; right: 0;
    font-size: 22px; font-weight: 700; letter-spacing: 1px;
  }
  .person-role-row {
    position: absolute; top: 72px; left: 0; right: 0;
    display: flex; align-items: center; gap: 10px;
  }
  .person-role-row .rule { flex: 1; height: 1px; background: var(--rule); }
  .person-role { font-size: 10px; color: var(--ink-soft); white-space: nowrap; }
  .icon-row {
    position: absolute; top: 108px; left: 0; right: 0;
    display: flex; justify-content: center; gap: 6px;
  }
  .icon-row svg { width: 20px; height: 20px; }
  .contact-list {
    position: absolute; top: 138px; left: 0; right: 0;
    list-style: none; font-size: 14.5px; line-height: 22px; font-weight: 500;
  }
  .bottom-rule {
    position: absolute; left: 0; right: 0; bottom: 40px;
    height: 1px; background: var(--rule);
  }

  /* brand side */
  .brand-lockup {
    position: absolute; left: 0; right: 0; top: 120px;
    display: flex; align-items: center; justify-content: center; gap: 16px;
  }
  .brand-dot { width: 26px; height: 26px; border-radius: 50%; background: var(--ink); }
  .brand-name { font-size: 42px; font-weight: 700; letter-spacing: .5px; }
  .brand-site {
    position: absolute; left: 0; right: 0; bottom: 40px;
    text-align: center; font-size: 13px; font-weight: 500;
  }
</style>
</head>
<body>
<main class="sheet">
  <section class="card card--contact">
    <h1 class="person-name">ROBIN HALE</h1>
    <div class="person-role-row">
      <span class="rule"></span>
      <span class="person-role">Senior. Business Development officer</span>
      <span class="rule"></span>
    </div>
    <div class="icon-row" aria-hidden="true">
      <svg viewBox="0 0 20 20" fill="none" stroke="#fff" stroke-width="1.2"><circle cx="10" cy="10" r="9"/><path d="M7 5.5l1.6 2.2-1 1.2c.7 1.4 1.8 2.5 3.2 3.2l1.2-1 2.2 1.6-.8 1.6c-3.8-.4-7.2-3.8-7.6-7.6z" fill="#fff"/></svg>
      <svg viewBox="0 0 20 20" fill="none" stroke="#fff" stroke-width="1.2"><circle cx="10" cy="10" r="9"/><rect x="5.5" y="7" width="9" height="6.5"/><path d="M5.5 7l4.5 3.5L14.5 7"/></svg>
      <svg viewBox="0 0 20 20" fill="none" stroke="#fff" stroke-width="1.2"><circle cx="10" cy="10" r="9"/><circle cx="10" cy="10" r="4.8"/><path d="M5.2 10h9.6M10 5.2c-2 2.6-2 7 0 9.6M10 5.2c2 2.6 2 7 0 9.6"/></svg>
      <svg viewBox="0 0 20 20" fill="none" stroke="#fff" stroke-width="1.2"><circle cx="10" cy="10" r="9"/><path d="M10 15s-3.5-3.6-3.5-6.2a3.5 3.5 0 017 0C13.5 11.4 10 15 10 15z"/><circle cx="10" cy="8.8" r="1.2"/></svg>
    </div>
    <ul class="contact-list">
      <li>(08) 8712 4590</li>
      <li>beaconserve@frostmail.example</li>
      <li>www.beaconchillworks.example.au</li>
      <li>Shed 5/218 Kestrel Rd ,Port Larkin SA 5790</li>
      <li>AU61924 , BLD402613</li>
    </ul>
    <span class="bottom-rule"></span>
  </section>

  <section class="card card--brand">
    <div class="brand-lockup">
      <span class="brand-dot"></span>
      <span class="brand-name">Beacon Chillworks</span>
    </div>
    <p class="brand-site">www.beaconchillworks.example.au</p>
  </section>
</main>
</body>
</html>
```